Business Card Design for company

We want new business cards. We'd like something different-- yet still highly professional. Our tagline is Providing leadership, delivering success. Stock photos are ok, as long as they are relevant and look upscale.

Target Market(s)

Architecture/Business Management Consulting/Engineering Consulting

Contact Information for Business Card

dark gray background with pops of blue might be good, but you tell me. You're the designers. Rounded corners might be nice, but again, you tell me.

Font styles to use
Serif
Sans Serif

Colors
3276b5
5c5c5c
9d9d9d
fbfbfb

Requirements
Nice to have
• Something different, but still very professional.

```html
<!DOCTYPE html>
<html lang="en">
<head>
<meta charset="utf-8">
<title>Veltra Global – Business Cards</title>
<link rel="stylesheet" href="https://fonts.googleapis.com/css2?family=Montserrat:wght@400;500;600&family=Open+Sans:wght@400;600&display=swap">
<style>
  :root {
    --bg: #2a2a2c;
    --card-dark: #141416;
    --card-light: #fbfbfb;
    --blue: #3276b5;
    --blue-band: #2a6398;
    --blue-deep: #1f4f7c;
    --gray-dark: #5c5c5c;
    --gray-mid: #9d9d9d;
    --ink: #2b2b2b;
    --white: #ffffff;
  }
  html, body {
    margin: 0;
    padding: 0;
    width: 1200px;
    height: 716px;
    overflow: hidden;
    background: var(--bg);
  }
  .stage {
    position: relative;
    width: 1200px;
    height: 716px;
    display: flex;
    align-items: center;
    justify-content: center;
    gap: 60px;
  }
  .card {
    width: 520px;
    height: 300px;
    border-radius: 18px;
    position: relative;
    overflow: hidden;
    box-shadow: 0 12px 30px rgba(0,0,0,0.45);
  }
  .card--front {
    background: var(--card-dark);
    display: flex;
    flex-direction: column;
    align-items: center;
    justify-content: center;
  }
  .brand-name {
    font-family: "Montserrat", sans-serif;
    font-weight: 500;
    font-size: 40px;
    letter-spacing: 6px;
    color: var(--blue);
    margin: 0;
  }
  .tagline {
    font-family: "Open Sans", sans-serif;
    font-size: 15px;
    color: var(--blue);
    margin: 22px 0 0;
    letter-spacing: 0.3px;
  }
  .card--back { background: var(--card-light); }
  .card--back svg { display: block; }
  .holder-name {
    font-family: "Montserrat", sans-serif;
    font-size: 22px;
    fill: var(--ink);
  }
  .holder-name .first { font-weight: 600; }
  .job-title {
    font-family: "Montserrat", sans-serif;
    font-size: 13px;
    letter-spacing: 1px;
    fill: var(--blue);
  }
  .brand-mark {
    font-family: "Montserrat", sans-serif;
    font-weight: 500;
    font-size: 22px;
    letter-spacing: 3px;
    fill: var(--blue);
  }
  .contact {
    font-family: "Open Sans", sans-serif;
    font-size: 13px;
    fill: var(--white);
  }
  .icon { fill: var(--blue-deep); }
</style>
</head>
<body>
<main class="stage">
  <section class="card card--front">
    <p class="brand-name">VELTRA GLOBAL</p>
    <p class="tagline">Providing leadership. Delivering success</p>
  </section>

  <section class="card card--back">
    <svg width="520" height="300" viewBox="0 0 520 300" xmlns="http://www.w3.org/2000/svg">
      <text class="holder-name" x="36" y="60"><tspan class="first">YOUR</tspan> NAME</text>
      <text class="job-title" x="36" y="78">JOB TITLE</text>

      <text class="brand-mark" x="480" y="148" text-anchor="end">VELTRA GLOBAL</text>

      <!-- contact band with tabs -->
      <path class="band" fill="var(--blue-band)"
        d="M0 172 H66 L74 158 H112 L120 172 H236 L244 158 H282 L290 172 H406 L414 158 H452 L460 172 H520 V300 H0 Z"/>
      <rect class="address-strip" x="0" y="222" width="520" height="26" fill="var(--gray-dark)"/>

      <!-- phone icon -->
      <g class="icon" transform="translate(93 168)">
        <path d="M-7 -3 Q-7 -6 -3 -6 H3 Q7 -6 7 -3 V-1 H4 V-3 H-4 V-1 H-7 Z"/>
        <rect x="-5" y="0" width="10" height="5" rx="1"/>
      </g>
      <!-- mail icon -->
      <g class="icon" transform="translate(263 168)">
        <rect x="-7" y="-5" width="14" height="10" rx="1"/>
        <path d="M-7 -5 L0 1 L7 -5" fill="none" stroke="var(--blue-band)" stroke-width="1.2"/>
      </g>
      <!-- globe icon -->
      <g transform="translate(433 168)">
        <circle r="6" class="icon"/>
        <path d="M-6 0 H6 M0 -6 V6" stroke="var(--blue-band)" stroke-width="1" fill="none"/>
      </g>

      <text class="contact" x="93" y="203" text-anchor="middle">000 000 0000</text>
      <text class="contact" x="263" y="203" text-anchor="middle">youremail@xyz.com</text>
      <text class="contact" x="433" y="203" text-anchor="middle">yourwebsite.com</text>

      <!-- pin icon -->
      <path fill="var(--blue)" d="M176 229 a5 5 0 0 1 5 5 c0 4 -5 9 -5 9 c0 0 -5 -5 -5 -9 a5 5 0 0 1 5 -5 Z"/>
      <circle cx="176" cy="234" r="1.8" fill="var(--gray-dark)"/>
      <text class="contact" x="188" y="240">Your Address here, City, ST 0000</text>
    </svg>
  </section>
</main>
</body>
</html>
```